Company identity deisgn should support 2 languages

I would like to get our company identity design
This includes the following only
Business Cards 2 languages Arabic and English
Email signature
Letterhead
Linkedin profile images
Attached is the logo in Ai format

Requirements
Must have
• For business card
Must have
Name and Adrees in arabic
Name and Address in english
You might use both side of the card
Should not have
• Any pictures other than the logo

```html
<!DOCTYPE html>
<html lang="en">
<head>
<meta charset="utf-8">
<title>Business Cards – English / Arabic</title>
<link href="https://fonts.googleapis.com/css2?family=Poppins:wght@400;600&family=Cairo:wght@400;700&display=swap" rel="stylesheet">
<style>
  :root{
    --brand-blue:#1077c0;
    --paper:#ffffff;
    --backdrop:#e6e7e8;
    --ink-light:#ffffff;
    --logo-blue:#1a7cc7;
  }
  html,body{margin:0;padding:0;width:1200px;height:1200px;overflow:hidden;background:var(--backdrop);}
  .sheet{position:relative;width:1200px;height:1200px;}
  .card{
    position:absolute;left:200px;width:800px;height:457px;
    background:var(--paper);border-radius:24px;overflow:hidden;
    box-shadow:0 10px 24px rgba(0,0,0,.18);
  }
  .card--front{top:140px;}
  .card--back{top:620px;}
  .card__band{position:absolute;inset:0;width:800px;height:457px;}
  .card__band path{fill:var(--brand-blue);}
  .brand{
    position:absolute;top:88px;right:56px;display:flex;align-items:center;gap:14px;
    font-family:"Poppins",sans-serif;font-weight:600;font-size:24px;letter-spacing:.5px;
    color:var(--logo-blue);
  }
  .brand__dot{width:34px;height:34px;border-radius:50%;background:var(--logo-blue);}
  .details{position:absolute;left:50px;top:172px;color:var(--ink-light);font-family:"Poppins",sans-serif;}
  .details__name{margin:0;font-size:26px;font-weight:600;line-height:32px;}
  .details__role{margin:0;font-size:18px;line-height:22px;}
  .details__address{margin:16px 0 0;font-size:18px;line-height:22px;font-style:normal;}
  .contact{list-style:none;margin:16px 0 0;padding:0;}
  .contact li{display:flex;align-items:center;gap:10px;font-size:18px;line-height:22.5px;}
  .contact svg{width:16px;height:16px;fill:var(--ink-light);flex:none;}
  .details--ar{left:44px;top:174px;}
  .details--ar .details__name,.details--ar .details__role,.details--ar .details__address{font-family:"Cairo",sans-serif;}
  .details--ar .details__name{font-size:26px;font-weight:700;line-height:30px;}
  .details--ar .details__role{font-size:19px;line-height:22px;}
  .details--ar .details__address{font-size:17px;line-height:27px;margin-top:12px;}
  .details--ar .contact{margin-top:10px;}
  .details--ar .contact li{font-size:17px;}
  .ar{direction:rtl;unicode-bidi:isolate;text-align:left;display:block;}
</style>
</head>
<body>
<svg width="0" height="0" style="position:absolute" aria-hidden="true">
  <defs>
    <symbol id="icon-phone" viewBox="0 0 16 16"><path d="M3.2 1.2l2.4-.4 1.3 3.3-1.5 1.2c.8 1.8 2 3 3.8 3.9l1.2-1.5 3.3 1.3-.4 2.4c-.2.9-1 1.4-1.9 1.3C6.5 12.2 3.8 9.5 2 4.4c-.3-.9.3-2.9 1.2-3.2z"/></symbol>
    <symbol id="icon-mobile" viewBox="0 0 16 16"><path d="M4 0h8a1 1 0 0 1 1 1v14a1 1 0 0 1-1 1H4a1 1 0 0 1-1-1V1a1 1 0 0 1 1-1zm.6 1.6v11.2h6.8V1.6z"/></symbol>
    <symbol id="icon-fax" viewBox="0 0 16 16"><path d="M4 1h7l1 1v4H4zM1 7h14v6H1zM3 14h10v1.5H3zM11 9h2v1.2h-2z"/></symbol>
    <symbol id="icon-mail" viewBox="0 0 16 16"><path d="M1 3.5h14v9H1zm1.3 1.2L8 9l5.7-4.3z" fill-rule="evenodd"/></symbol>
    <symbol id="icon-globe" viewBox="0 0 16 16"><path d="M8 1a7 7 0 1 0 0 14A7 7 0 0 0 8 1zm-1 2.5c1 .3 1.6 1 1.3 1.9-.4.9-1.8.7-2 1.9-.2 1.1 1.3 1.2 1.3 2.5 0 1-.8 1.4-1 2.7-2-.7-3.4-2.6-3.4-4.7 0-2 1.5-3.8 3.8-4.3zm4.5 5.3c.7.2 1 1 .8 1.8-.3.8-1.2 1.3-1.8.9-.5-.4-.1-1.2.2-1.8.2-.5.4-.9.8-.9z"/></symbol>
  </defs>
</svg>

<main class="sheet">
  <section class="card card--front" lang="en">
    <svg class="card__band" viewBox="0 0 800 457" aria-hidden="true">
      <path d="M0 0 H195 C225 0 240 20 266 56 L482 385 C505 424 522 436 560 418 L570 413 L555 457 H0 Z"/>
    </svg>
    <div class="brand"><span class="brand__dot"></span>NORTHWIND COGNITIVE</div>
    <div class="details">
      <h1 class="details__name">DANIEL HARPER</h1>
      <p class="details__role">President</p>
      <address class="details__address">2140 Willow Crest Road<br>Fairbanks, Alaska 99701</address>
      <ul class="contact">
        <li><svg><use href="#icon-phone"/></svg>555-214-7730</li>
        <li><svg><use href="#icon-mobile"/></svg>555-308-6142</li>
        <li><svg><use href="#icon-fax"/></svg>555-471-2296</li>
        <li><svg><use href="#icon-mail"/></svg>info@northwindcognitive.com</li>
        <li><svg><use href="#icon-globe"/></svg>www.northwindcognitive.com</li>
      </ul>
    </div>
  </section>

  <section class="card card--back">
    <svg class="card__band" viewBox="0 0 800 457" aria-hidden="true">
      <path d="M0 0 H195 C225 0 240 20 266 56 L482 385 C505 424 522 436 560 418 L570 413 L555 457 H0 Z"/>
    </svg>
    <div class="brand"><span class="brand__dot"></span>NORTHWIND COGNITIVE</div>
    <div class="details details--ar">
      <h2 class="details__name" lang="ar"><span class="ar">دانيال هاربر</span></h2>
      <p class="details__role" lang="ar"><span class="ar">رئيس</span></p>
      <address class="details__address" lang="ar"><span class="ar">2140 ويلو كريست</span><span class="ar">فيربانكس ، ألاسكا 99701</span></address>
      <ul class="contact">
        <li><svg><use href="#icon-phone"/></svg>555-214-7730</li>
        <li><svg><use href="#icon-mobile"/></svg>555-308-6142</li>
        <li><svg><use href="#icon-fax"/></svg>555-471-2296</li>
        <li><svg><use href="#icon-mail"/></svg>info@northwindcognitive.com</li>
        <li><svg><use href="#icon-globe"/></svg>www.northwindcognitive.com</li>
      </ul>
    </div>
  </section>
</main>
</body>
</html>
```